Mobile welding fabrication and repair, heavy equipment and semi repair

We need a business card design that will catch the eye but look prelesional at the same time. Were based out of Idaho and we do all welding fabrication jobs and repairs, we also build and install custom pipe fences for personal or larger scale fence jobs and can give free quotes. We can do semi truck and trailer repairs Mobily also.

Target Market(s)

Welding

Industry/Entity Type

welding and repair

Contact Information for Business Card

email (flintforgeandfix@mailvero.com, phone number 208-417-3862, owner (Wade Pellston), Pipe Fence, Semi Repair, Mobile welding and fabrication

Font styles to use
Sans Serif

Requirements
Must have
• My logo in black background on one side , and other side my logo in white back round with all the information listed on card details
Nice to have
• make it stand out from other business cards

```html
<!DOCTYPE html>
<html lang="en">
<head>
<meta charset="UTF-8">
<title>Flint Forge and Fix – Business Card</title>
<link rel="stylesheet" href="https://fonts.googleapis.com/css2?family=Montserrat:wght@400;500;700;800&display=swap">
<style>
  :root {
    --backdrop: #c9c9c9;
    --card-white: #ffffff;
    --card-dark: #2b2b2b;
    --card-dark-edge: #1c1c1c;
    --brand-blue: #1f63b8;
    --rule-blue: #4a7fc8;
    --ink: #2a2a2a;
    --ink-soft: #444;
  }
  * { box-sizing: border-box; margin: 0; padding: 0; }
  html, body { width: 1200px; height: 788px; overflow: hidden; }
  body {
    background: var(--backdrop);
    font-family: "Montserrat", sans-serif;
    position: relative;
  }
  .card {
    position: absolute;
    top: 240px;
    width: 540px;
    height: 309px;
    border-radius: 24px;
    overflow: hidden;
    box-shadow: 0 14px 30px rgba(0,0,0,0.25);
  }
  .card--front { left: 40px; background: var(--card-white); }
  .card--back { left: 620px; background: var(--card-dark); }

  .brand-mark {
    position: absolute;
    right: 34px;
    top: 34px;
    text-align: right;
    color: var(--brand-blue);
    font-weight: 800;
    letter-spacing: 1px;
    line-height: 1.05;
  }
  .brand-mark__main { display: block; font-size: 34px; }
  .brand-mark__sub { display: block; font-size: 15px; letter-spacing: 2px; }

  .services {
    position: absolute;
    right: 34px;
    top: 116px;
    text-align: right;
    list-style: none;
    font-size: 12px;
    color: var(--ink);
    line-height: 1.45;
  }
  .services li::after { content: " •"; color: var(--brand-blue); }

  .owner {
    position: absolute;
    left: 30px;
    top: 160px;
  }
  .owner__name {
    font-size: 22px;
    font-weight: 700;
    color: var(--brand-blue);
    letter-spacing: 1px;
    text-transform: uppercase;
  }
  .owner__role { font-size: 12px; color: var(--ink-soft); margin-top: 2px; }

  .divider {
    position: absolute;
    left: 30px;
    right: 90px;
    top: 210px;
    height: 1px;
    background: var(--rule-blue);
  }

  .contact {
    position: absolute;
    left: 30px;
    top: 222px;
    list-style: none;
    font-size: 12.5px;
    color: var(--ink);
    line-height: 1.55;
  }
  .contact li { display: flex; align-items: center; gap: 8px; }
  .contact svg { width: 11px; height: 11px; fill: var(--brand-blue); flex: none; }

  .back-texture {
    position: absolute;
    inset: 0;
    background: radial-gradient(ellipse at 80% 20%, #4a4a4a 0%, var(--card-dark) 45%, var(--card-dark-edge) 100%);
  }
  .back-mark {
    position: absolute;
    right: 34px;
    bottom: 34px;
    text-align: right;
    color: var(--brand-blue);
    font-weight: 800;
    letter-spacing: 1px;
    line-height: 1.05;
  }
  .back-mark .brand-mark__main { font-size: 30px; }
  .back-mark .brand-mark__sub { font-size: 13px; }
</style>
</head>
<body>
  <section class="card card--front">
    <div class="brand-mark">
      <span class="brand-mark__main">FLINT FORGE</span>
      <span class="brand-mark__sub">AND FIX</span>
    </div>
    <ul class="services">
      <li>Pipe Fence</li>
      <li>Semi Repair</li>
      <li>Mobile welding and fabrication</li>
    </ul>
    <div class="owner">
      <div class="owner__name">Wade Pellston</div>
      <div class="owner__role">Owner</div>
    </div>
    <div class="divider"></div>
    <ul class="contact">
      <li><svg viewBox="0 0 24 24"><path d="M6.6 10.8a15.1 15.1 0 0 0 6.6 6.6l2.2-2.2a1 1 0 0 1 1-.25 11.4 11.4 0 0 0 3.6.57 1 1 0 0 1 1 1V20a1 1 0 0 1-1 1A17 17 0 0 1 3 4a1 1 0 0 1 1-1h3.5a1 1 0 0 1 1 1c0 1.25.2 2.45.57 3.57a1 1 0 0 1-.25 1z"/></svg>208-417-3862</li>
      <li><svg viewBox="0 0 24 24"><path d="M2 5h20v14H2z M2 5l10 8 10-8" /></svg>flintforgeandfix@mailvero.com</li>
      <li><svg viewBox="0 0 24 24"><circle cx="12" cy="12" r="10"/></svg>www.flintforgeandfix.ch</li>
    </ul>
  </section>

  <section class="card card--back">
    <div class="back-texture" role="img" aria-label="Repeating pattern of the brand symbol in dark grey tones"></div>
    <div class="back-mark">
      <span class="brand-mark__main">FLINT FORGE</span>
      <span class="brand-mark__sub">AND FIX</span>
    </div>
  </section>
</body>
</html>
```